Business Card Design for BrightlaneReach.com

--I need a business card design for my company BrightlaneReach.com

I have attached my logo...I want the brightlane reach logo on the front of the business card, and then I want The Brightlane Chief on the back of it with my information.

I would like to see a light colored background as well as a dark colored background

FRONT:
BRIGHTLANE REACH LOGO
247 E. Pelham Row
5th Floor
San Diego CA 92384
www.BrightlaneReach.com

Advanced Website & App Development
Websites, Apps, Online Voucher Systems

Leading Edge Marketing Services
SMS, VB, SMM, SEM,

BACK:
BRIGHTLANE CHIEF LOGO
Dorian Welker
The Brightlane Chief
Call Or Text: 555-204-3378
Dorian@BrightlaneChief.com
www.BrightlaneChief.com

Target Market(s)

small business owners

Industry/Entity Type

Business Consultant

Contact Information for Business Card

FRONT:
BRIGHTLANE REACH LOGO
247 E. Pelham Row
5th Floor
San Diego CA 92384
www.BrightlaneReach.com

SMS, VB, SMM, SEM,

BACK:
BRIGHTLANE CHIEF LOGO
Dorian Welker
The Brightlane Chief
Dorian@BrightlaneChief.com
www.BrightlaneChief.com

Requirements
Must have
• add this quote on it somewhere, anywhere,preferrably on back
• "The Fastest Way To Success Is To Take Action”
• — Dorian Welker, Brightlane Chief
Nice to have
• open
Should not have
• red

```html
<!DOCTYPE html>
<html lang="en">
<head>
<meta charset="utf-8">
<title>Brightlane Reach Business Cards</title>
<link href="https://fonts.googleapis.com/css2?family=Roboto+Condensed:wght@300;400;700&display=swap" rel="stylesheet">
<style>
  :root {
    --navy: #07344a;
    --blue: #1777b0;
    --sage: #9dc8a7;
    --gray: #6e7275;
    --white: #ffffff;
    --canvas: #ffffff;
  }
  * { margin: 0; padding: 0; box-sizing: border-box; }
  html, body {
    width: 1200px; height: 721px; overflow: hidden;
    background: var(--canvas);
    font-family: "Roboto Condensed", "Arial Narrow", sans-serif;
  }
  .sheet { position: relative; width: 1200px; height: 721px; }
  .card {
    position: absolute; width: 564px; height: 326px;
    border-radius: 32px; text-align: center;
  }
  .card--dark { background: var(--navy); }
  .card--light { background: var(--sage); }
  .pos-tl { left: 24px; top: 28px; }
  .pos-tr { left: 611px; top: 28px; }
  .pos-bl { left: 24px; top: 368px; }
  .pos-br { left: 611px; top: 368px; }

  .brand-name {
    position: absolute; left: 0; right: 0;
    font-weight: 400; font-size: 42px; letter-spacing: 4px;
    color: var(--blue); line-height: 1;
  }
  .front .brand-name { top: 56px; }
  .back .brand-name { top: 56px; }

  .services {
    position: absolute; left: 0; right: 0;
    font-weight: 300; font-size: 17.5px; color: var(--gray); line-height: 1;
  }
  .services--headline { top: 161px; }
  .services--list { top: 187px; }
  .services--marketing { top: 223px; }
  .dot { color: var(--blue); padding: 0 3px; }

  .info-band {
    position: absolute; left: 62px; width: 440px; top: 254px; height: 49px;
    border-radius: 9px; color: var(--white);
    font-weight: 300; font-size: 16.5px; line-height: 21px;
    padding-top: 3px;
  }
  .card--dark .info-band { background: var(--blue); }
  .card--light .info-band { background: var(--navy); }
  .card--dark .info-band .dot { color: var(--navy); }

  .person-name {
    position: absolute; left: 0; right: 0; top: 140px;
    font-weight: 700; font-size: 31px; line-height: 1; letter-spacing: 0.3px;
  }
  .card--dark .person-name { color: var(--white); }
  .card--light .person-name { color: var(--navy); }
  .person-title {
    position: absolute; left: 0; right: 0; top: 176px;
    font-weight: 300; font-size: 19px; color: var(--gray); line-height: 1;
  }
  .quote {
    position: absolute; left: 40px; right: 40px; top: 212px;
    font-weight: 300; font-size: 14.5px; line-height: 1.25;
  }
  .card--dark .quote { color: var(--white); }
  .card--light .quote { color: var(--navy); }
  .quote cite { font-style: normal; color: var(--gray); }
</style>
</head>
<body>
<main class="sheet">
  <section class="card card--dark front pos-tl">
    <div class="brand-name">BRIGHTLANE REACH</div>
    <p class="services services--headline">Advanced Website &amp; App Development</p>
    <p class="services services--list">Websites <span class="dot">•</span> Apps <span class="dot">•</span> Online Voucher Systems</p>
    <p class="services services--marketing">Leading Edge Marketing Services: SMS <span class="dot">•</span> VB <span class="dot">•</span> SMM <span class="dot">•</span> SEM</p>
    <div class="info-band">247 E. Pelham Row, 5th Floor, San Diego CA 92384<br>www.BrightlaneReach.com</div>
  </section>

  <section class="card card--light front pos-tr">
    <div class="brand-name">BRIGHTLANE REACH</div>
    <p class="services services--headline">Advanced Website &amp; App Development</p>
    <p class="services services--list">Websites <span class="dot">•</span> Apps <span class="dot">•</span> Online Voucher Systems</p>
    <p class="services services--marketing">Leading Edge Marketing Services: SMS <span class="dot">•</span> VB <span class="dot">•</span> SMM <span class="dot">•</span> SEM</p>
    <div class="info-band">247 E. Pelham Row, 5th Floor, San Diego CA 92384<br>www.BrightlaneReach.com</div>
  </section>

  <section class="card card--dark back pos-bl">
    <div class="brand-name">BRIGHTLANE CHIEF</div>
    <h1 class="person-name">DORIAN WELKER</h1>
    <p class="person-title">The Brightlane Chief</p>
    <blockquote class="quote">“The Fastest Way To Success Is To Take Action”<br><cite>— Dorian Welker, Brightlane Chief</cite></blockquote>
    <div class="info-band">Call Or Text: 555-204-3378<br>Dorian@BrightlaneChief.com <span class="dot">•</span> www.BrightlaneChief.com</div>
  </section>

  <section class="card card--light back pos-br">
    <div class="brand-name">BRIGHTLANE CHIEF</div>
    <h2 class="person-name">DORIAN WELKER</h2>
    <p class="person-title">The Brightlane Chief</p>
    <blockquote class="quote">“The Fastest Way To Success Is To Take Action”<br><cite>— Dorian Welker, Brightlane Chief</cite></blockquote>
    <div class="info-band">Call Or Text: 555-204-3378<br>Dorian@BrightlaneChief.com <span class="dot">•</span> www.BrightlaneChief.com</div>
  </section>
</main>
</body>
</html>
```